Real Estate "For Sale" Sign for construction company

We need a sign that we can use to hang on a post and place on the road when we sell a property. The sign will be simple and will need to mainly feature our logo (files attached), as well as the words "For Sale", and then our phone number "(555) 617 3489". The sign will hang on a post that'll look something like the attached picture.

Target Market(s)

Home buyers

Industry/Entity Type

Real Estate

Font styles to use
Serif
Sans Serif

Colors
0054AA
0677BA
7BADD7
CADEEF
E8F1F8
0094D4
00A9DD
6FCCEA
C7EBF8
E9F6FB

Requirements
Must have
• For Sale & our phone number

```html
<!DOCTYPE html>
<html lang="en">
<head>
<meta charset="utf-8">
<title>For Sale Sign – Hollow Pine Realty</title>
<link rel="stylesheet" href="https://fonts.googleapis.com/css2?family=Montserrat:wght@500;700;800&family=Poppins:wght@400;500&display=swap">
<style>
  :root {
    --backdrop: #5f93a3;
    --navy: #141f4a;
    --sky: #45c6f2;
    --white: #ffffff;
    --brand-blue: #1a7cc2;
    --footer-blue: #167fc4;
    --art-light: #1a82c7;
    --art-mid: #0054aa;
    --art-deep: #253a7c;
  }
  * { box-sizing: border-box; margin: 0; padding: 0; }
  html, body {
    width: 1200px; height: 1200px; overflow: hidden;
    background: var(--backdrop);
  }
  .canvas {
    position: relative; width: 1200px; height: 1200px;
    display: flex; align-items: center; justify-content: center;
  }
  .sign {
    position: relative; width: 820px; height: 1100px;
    background: var(--white); overflow: hidden;
  }
  .sign-header {
    position: absolute; left: 0; top: 0; width: 100%; height: 680px;
    background: var(--navy); overflow: hidden;
  }
  .header-art {
    position: absolute; left: 360px; top: 27px; width: 460px; height: 350px;
    background: linear-gradient(180deg, var(--art-light) 0%, var(--art-mid) 55%, var(--art-deep) 100%);
    z-index: 0;
  }
  .headline {
    position: absolute; left: 104px; top: 78px; z-index: 1;
    font-family: "Montserrat", sans-serif; font-weight: 700;
    font-size: 178px; line-height: 160px; letter-spacing: -2px;
  }
  .headline .word-for { display: block; color: var(--sky); }
  .headline .word-sale { display: block; color: var(--white); }
  .divider {
    position: absolute; left: 95px; right: 0; top: 459px; height: 6px;
    background: var(--sky);
  }
  .contact {
    position: absolute; left: 92px; top: 528px;
    display: flex; align-items: center; gap: 46px;
  }
  .contact-icon { width: 76px; height: 76px; }
  .contact-number {
    font-family: "Poppins", sans-serif; font-weight: 500;
    font-size: 66px; color: var(--white); letter-spacing: 0;
  }
  .brand {
    position: absolute; left: 0; top: 680px; width: 100%; height: 338px;
    display: flex; align-items: center; justify-content: center; gap: 20px;
  }
  .brand-dot {
    width: 36px; height: 36px; border-radius: 50%; background: var(--brand-blue);
  }
  .brand-name {
    font-family: "Montserrat", sans-serif; font-weight: 500;
    font-size: 52px; color: var(--brand-blue);
  }
  .sign-footer {
    position: absolute; left: 0; bottom: 0; width: 100%; height: 82px;
    background: var(--footer-blue);
    display: flex; align-items: center; justify-content: center;
    font-family: "Poppins", sans-serif; font-weight: 400;
    font-size: 25px; color: var(--white);
  }
</style>
</head>
<body>
<main class="canvas">
  <section class="sign">
    <div class="sign-header">
      <div class="header-art" role="img" aria-label="Decorative illustration of layered blue mountain ridges"></div>
      <h1 class="headline"><span class="word-for">FOR</span><span class="word-sale">SALE</span></h1>
      <div class="divider"></div>
      <div class="contact">
        <svg class="contact-icon" viewBox="0 0 80 80" aria-hidden="true">
          <path d="M14 10 q-10 6 -6 20 q8 24 30 40 q12 8 20 -2 l4 -5 q2 -4 -2 -7 l-10 -8 q-4 -3 -8 1 l-4 4 q-12 -6 -20 -20 l4 -4 q4 -4 1 -8 l-7 -11 q-3 -4 -7 -1 z" fill="none" stroke="var(--sky)" stroke-width="6" stroke-linejoin="round"/>
          <path d="M44 22 q12 2 14 14" fill="none" stroke="var(--sky)" stroke-width="6" stroke-linecap="round"/>
          <path d="M46 8 q24 4 28 28" fill="none" stroke="var(--sky)" stroke-width="6" stroke-linecap="round"/>
        </svg>
        <span class="contact-number">(555) 617 3489</span>
      </div>
    </div>
    <div class="brand">
      <span class="brand-dot"></span>
      <span class="brand-name">Hollow Pine Realty</span>
    </div>
    <footer class="sign-footer">www.hollowpinerealty.com</footer>
  </section>
</main>
</body>
</html>
```